The Harbourgate Clinic Stationary (Medical)

Stationery for The Harbourgate clinic
using existing logos
Please also add a green apple if possible on another corner away from the logo on some of your designs

Please take a look at www.theharbourgateclinic.com.au so you can get a feel for what The Harbourgate Clinic offers our clients.

Stationary Required: business cards, letter head, comp slips

I do not require envelopes or invoives.
Updates

Target Market(s)

The general popultation needing medical care
Professionals
Mums & Dads
Elderly

Industry/Entity Type

Business

Requirements
Must have
• Company Logo

Address
Email
Website
Phone
Should not have
• Traditional Medical Icons
No Times New Roman

```html
<!DOCTYPE html>
<html lang="en">
<head>
<meta charset="utf-8">
<title>The Harbourgate Clinic – Stationery</title>
<link rel="stylesheet" href="https://fonts.googleapis.com/css2?family=Arimo:wght@400;700&display=swap">
<style>
  :root {
    --cyan: #3ccdf2;
    --green: #8dc63f;
    --ink: #1a1a1a;
    --paper: #ffffff;
    --edge: #d6d6d6;
    --apple-a: #dfeeb8;
    --apple-b: #f3f8e6;
  }
  * { box-sizing: border-box; margin: 0; padding: 0; }
  html, body { width: 1200px; height: 900px; overflow: hidden; background: #fff; }
  body { font-family: "Arimo", Arial, sans-serif; color: var(--ink); position: relative; }

  .sheet {
    position: absolute; background: var(--paper);
    box-shadow: 0 0 0 1px var(--edge), 2px 3px 6px rgba(0,0,0,.12);
    overflow: hidden;
  }
  .wedge { position: absolute; left: 0; width: 100%; }
  .apple {
    position: absolute; border-radius: 50%;
    background: radial-gradient(circle at 45% 40%, var(--apple-b), var(--apple-a) 70%);
    opacity: .85;
  }

  .brand { position: absolute; display: flex; align-items: center; gap: 8px; }
  .brand-dot { width: 22px; height: 22px; border-radius: 50%; background: var(--green); flex: none; }
  .brand-name { color: var(--cyan); font-weight: 700; line-height: 1.05; }
  .brand-tag { color: var(--ink); font-size: 8px; line-height: 1.25; margin-top: 3px; }

  .contact { position: absolute; font-weight: 700; font-size: 12px; line-height: 1.55; text-align: right; white-space: nowrap; }

  /* Letterhead */
  .letterhead { left: 24px; top: 44px; width: 556px; height: 792px; }
  .letterhead .apple { left: -40px; top: -40px; width: 190px; height: 200px; }
  .letterhead .brand { right: 44px; top: 36px; }
  .letterhead .brand-name { font-size: 19px; }
  .letterhead .contact { right: 14px; top: 122px; }
  .letterhead-footer {
    position: absolute; left: 0; bottom: 0; width: 100%; height: 80px;
    background: var(--cyan); color: #fff; text-align: center;
    font-size: 12px; line-height: 1.5; padding-top: 10px;
  }

  /* Business card front */
  .card-front { left: 666px; top: 84px; width: 404px; height: 206px; }
  .card-front .brand { left: 20px; top: 30px; gap: 6px; }
  .card-front .brand-dot { width: 18px; height: 18px; }
  .card-front .brand-name { font-size: 13px; }
  .card-front .brand-tag { font-size: 7px; }
  .card-rule { position: absolute; left: 172px; top: 28px; width: 1px; height: 128px; background: var(--ink); }
  .card-details { position: absolute; left: 182px; top: 30px; font-size: 8.5px; font-weight: 700; line-height: 1.45; white-space: nowrap; }
  .card-details .gap { height: 6px; }
  .card-front .wedge { bottom: 0; height: 44px; }

  /* Business card back */
  .card-back { left: 666px; top: 310px; width: 404px; height: 260px; }
  .card-back .wedge { top: 0; height: 50px; }
  .card-back .brand { left: 118px; top: 96px; }
  .card-back .brand-name { font-size: 21px; }
  .card-back .apple { left: -30px; top: 168px; width: 130px; height: 130px; }

  /* Compliments slip */
  .comp-slip { left: 606px; top: 586px; width: 560px; height: 278px; }
  .comp-slip .wedge { top: 0; height: 82px; width: 300px; }
  .comp-label { position: absolute; left: 18px; top: 24px; color: #fff; font-size: 12px; font-weight: 700; letter-spacing: 2px; }
  .comp-slip .brand { right: 20px; top: 22px; }
  .comp-slip .brand-name { font-size: 17px; }
  .comp-slip .contact { right: 24px; top: 112px; font-size: 11px; }
  .comp-slip .apple { left: -40px; top: 190px; width: 130px; height: 130px; }
  .comp-address { position: absolute; left: 0; width: 100%; top: 226px; text-align: center; font-size: 11px; line-height: 1.45; }
</style>
</head>
<body>

  <section class="sheet letterhead" aria-label="Letterhead">
    <div class="apple" role="img" aria-label="Faint green apple illustration"></div>
    <div class="brand">
      <span class="brand-dot"></span>
      <div>
        <div class="brand-name">The Harbourgate<br>Clinic</div>
        <div class="brand-tag">Friendly Local Care<br>Close to Home</div>
      </div>
    </div>
    <p class="contact">Phone : 02 9000 4812<br>email : HR@theharbourgateclinic.com.au<br>Website : www.theharbourgateclinic.com.au</p>
    <footer class="letterhead-footer">
      Eastwood Ridge<br>
      The Harbourgate Clinic (Inside Bluewell Pharmacy)<br>
      Shop 14, Ridgeview Market Place, 6 - 18 The Ridgeline Parkway, Eastwood Ridge 2125
    </footer>
  </section>

  <section class="sheet card-front" aria-label="Business card front">
    <div class="brand">
      <span class="brand-dot"></span>
      <div>
        <div class="brand-name">The Harbourgate<br>Clinic</div>
        <div class="brand-tag">Friendly Local Care<br>Close to Home</div>
      </div>
    </div>
    <div class="card-rule"></div>
    <div class="card-details">
      Eastwood Ridge<br>
      The Harbourgate Clinic<br>
      (Inside Bluewell Pharmacy)<br>
      Shop 14, Ridgeview Market Place<br>
      6 - 18 The Ridgeline Parkway<br>
      Eastwood Ridge 2125
      <div class="gap"></div>
      Phone 02 9000 4812<br>
      email HR@theharbourgateclinic.com.au<br>
      Website www.theharbourgateclinic.com.au
    </div>
    <svg class="wedge" viewBox="0 0 404 44" preserveAspectRatio="none" aria-hidden="true">
      <polygon points="0,24 404,0 404,44 0,44" fill="var(--cyan)"/>
    </svg>
  </section>

  <section class="sheet card-back" aria-label="Business card back">
    <svg class="wedge" viewBox="0 0 404 50" preserveAspectRatio="none" aria-hidden="true">
      <polygon points="0,0 404,0 404,8 0,50" fill="var(--cyan)"/>
    </svg>
    <div class="brand">
      <span class="brand-dot"></span>
      <div>
        <div class="brand-name">The Harbourgate<br>Clinic</div>
        <div class="brand-tag">Friendly Local Care<br>Close to Home</div>
      </div>
    </div>
    <div class="apple" role="img" aria-label="Green apple illustration"></div>
  </section>

  <section class="sheet comp-slip" aria-label="Compliments slip">
    <svg class="wedge" viewBox="0 0 300 82" preserveAspectRatio="none" aria-hidden="true">
      <polygon points="0,0 300,0 300,14 0,82" fill="var(--cyan)"/>
    </svg>
    <span class="comp-label">WITH COMPLIMENTS</span>
    <div class="brand">
      <span class="brand-dot"></span>
      <div>
        <div class="brand-name">The Harbourgate<br>Clinic</div>
        <div class="brand-tag">Friendly Local Care<br>Close to Home</div>
      </div>
    </div>
    <p class="contact">Phone : 02 9000 4812<br>email : HR@theharbourgateclinic.com.au<br>Website : www.theharbourgateclinic.com.au</p>
    <div class="apple" role="img" aria-label="Green apple illustration"></div>
    <p class="comp-address">
      Eastwood Ridge<br>
      The Harbourgate Clinic (Inside Bluewell Pharmacy)<br>
      Shop 14, Ridgeview Market Place, 6 - 18 The Ridgeline Parkway, Eastwood Ridge 2125
    </p>
  </section>

</body>
</html>
```